Marketing Brochure: Category Management – Assortment Optimization

Create a compelling a 1-page marketing brochure around a service that allows Brill International retailers to optimize their product assortments in their stores. The brochure must be fun, very professionally done, clean, and exciting to want possible clients to want to pick up. See word file for content details. The Brill Worldwide Partners red and white colors should be used. Also, include relevant photos to liven up the brochure.

Target Market(s)

Brill Toolworks Retailers in Different Parts of the World

Industry/Entity Type

Retail

Font styles to use
Sans Serif

Requirements
Must have
• See Word file. Add some really good photos relevant to retail.
• Red and White Colors would be good to match Brill Worldwide Partners logo
• Also, should look like a 'global' service. Maybe add a worldly look to it.
Nice to have
• See World file
Should not have
• N/A

```html
<!DOCTYPE html>
<html lang="en">
<head>
<meta charset="utf-8">
<title>Brill Worldwide Partners – Category Management Brochure</title>
<link rel="stylesheet" href="https://fonts.googleapis.com/css2?family=Montserrat:wght@400;500;600;700&family=Oswald:wght@700&display=swap">
<style>
  :root {
    --red: #d71f2b;
    --red-dark: #8e1116;
    --ink: #222222;
    --black: #1c1b1b;
    --white: #ffffff;
    --stage: #d9d9d9;
    --wood-dark: #3b2a1d;
    --wood-mid: #6b4b31;
  }
  * { box-sizing: border-box; margin: 0; padding: 0; }
  html, body { width: 1200px; height: 1200px; overflow: hidden; }
  body {
    background: var(--stage);
    font-family: "Montserrat", Arial, sans-serif;
    color: var(--ink);
  }
  .brochure {
    position: absolute;
    left: 160px; top: 30px;
    width: 880px; height: 1140px;
    background: var(--white);
    overflow: hidden;
    box-shadow: 0 10px 30px rgba(0,0,0,.25);
  }
  .brand {
    position: absolute; left: 60px; top: 30px;
    display: flex; align-items: center; gap: 16px;
  }
  .brand-dot { width: 62px; height: 62px; border-radius: 50%; background: var(--red); }
  .brand-name { font-weight: 700; font-size: 30px; color: var(--black); line-height: 1; letter-spacing: -.3px; }
  .brand-tagline { font-weight: 700; font-size: 13px; color: var(--red); letter-spacing: 1.6px; margin-top: 8px; }

  .hero {
    position: absolute; left: 0; top: 122px; width: 880px; height: 340px;
    background: linear-gradient(135deg, #a03a6a 0%, var(--wood-mid) 30%, var(--wood-dark) 75%, #9a9a9a 100%);
  }
  .title-band {
    position: absolute; left: 0; top: 462px; width: 880px; height: 76px;
    background: linear-gradient(90deg, var(--red-dark), var(--red) 60%, var(--red-dark));
    display: flex; align-items: center; padding-left: 44px;
  }
  .title-band h1 {
    font-family: "Oswald", Impact, sans-serif; font-weight: 700;
    font-size: 34px; color: var(--white); letter-spacing: .6px; text-transform: uppercase;
  }

  .col { position: absolute; top: 562px; }
  .col-left { left: 44px; width: 400px; }
  .col-right { left: 470px; width: 370px; }
  h2 { font-size: 17px; font-weight: 700; color: var(--black); margin-bottom: 8px; }
  .section-head { font-size: 17px; font-weight: 600; line-height: 1.2; margin: 16px 0 8px; }
  .section-head .caps { text-transform: uppercase; }
  p { font-size: 12px; line-height: 1.42; text-align: justify; margin-bottom: 8px; }

  .ticks { list-style: none; margin-bottom: 12px; }
  .ticks li {
    position: relative; padding-left: 24px;
    font-size: 12px; line-height: 1.33; margin-bottom: 7px;
  }
  .ticks li::before {
    content: ""; position: absolute; left: 2px; top: 3px;
    width: 10px; height: 10px; border-radius: 50%; background: var(--red);
  }

  .web-strip { position: absolute; left: 420px; top: 1022px; width: 460px; height: 52px; }
  .web-strip span {
    position: absolute; right: 40px; top: 15px;
    color: var(--white); font-weight: 600; font-size: 17px; letter-spacing: 1.5px;
  }
  .call-bar {
    position: absolute; left: 0; top: 1074px; width: 880px; height: 66px;
    background: var(--black);
    display: flex; align-items: center; gap: 16px; padding-left: 60px;
    color: var(--white);
  }
  .call-bar .label { font-weight: 700; font-size: 34px; }
  .call-bar .number { font-weight: 700; font-size: 30px; letter-spacing: 1px; }
</style>
</head>
<body>
<main class="brochure">
  <header class="brand">
    <div class="brand-dot"></div>
    <div>
      <div class="brand-name">Brill Worldwide Partners</div>
      <div class="brand-tagline">PLAN | PARTNER | PROSPER</div>
    </div>
  </header>

  <div class="hero" role="img" aria-label="Photo of a wooden house cut-out framed by yellow folding rulers on a wood table, with a paint colour fan, brush, notebook, pen, compass and calculator"></div>

  <div class="title-band">
    <h1>Category Management – Assortment Optimization</h1>
  </div>

  <section class="col col-left">
    <h2>About Brill Worldwide Partners:</h2>
    <p>Brill Worldwide Partners is a Brill International consulting service that provides training and strategy recommendations based on Brill's 94-year retail industry expertise. Our services drive significant and sustainable performance improvements so you can accomplish your company's most important business objectives.</p>

    <h2 class="section-head"><span class="caps">Satisfying customers with data-</span><br>Driven, Informed Decisions</h2>
    <p>It takes a strong category strategy to drive sales growth. With changes in consumer demands and product introductions constantly making their way into the market, it's not easy to optimize product selection toward maximizing market share and wider profit margins. To do so, companies need to quickly and effectively deploy well-established and nimble methodologies that refine and enhance category assortment and retail space decisions.</p>
    <p>Brill Worldwide Partners category management's monthly services provides your business industry expertise, functional richness, and retail data analytics know-how to drive more profitable and productive product assortments. We speak analytics. In doing so, we synthesize raw data, assess it, and covert it into practical, measured solutions to help your business grow.</p>
  </section>

  <section class="col col-right">
    <h2>Our Service Approach:</h2>
    <ul class="ticks">
      <li>Understand your long-term vision, market and assortment objectives</li>
      <li>Assess the current state of affairs to your categories</li>
      <li>Obtain store level raw data one category at a time</li>
      <li>Covert raw data into powerful insights about category performance, opportunities, potential impact, and goal setting</li>
      <li>Implement recommendations, track results, and further advise</li>
    </ul>
    <h2>Return on Investment:</h2>
    <ul class="ticks">
      <li>Increased profitability and turnover</li>
      <li>Simplify assortments and planograms create a more consumer-friendly shopping experience</li>
      <li>Attack over-SKU'd categories &amp; less duplication</li>
      <li>Fact-based analytics with collaborative market insights</li>
      <li>Reduce wasteful spending and to help brands help retailers compete more effectively</li>
      <li>Acquired processes are safeguarded for the long-term</li>
      <li>The customer remains at the heart of decision making</li>
    </ul>
  </section>

  <div class="web-strip">
    <svg width="460" height="52" viewBox="0 0 460 52" aria-hidden="true">
      <polygon points="40,0 460,0 460,52 0,52" fill="#d71f2b"/>
    </svg>
    <span>www.bwpartnersgroup.com</span>
  </div>

  <footer class="call-bar">
    <span class="label">Call Us</span>
    <svg width="38" height="38" viewBox="0 0 38 38" aria-hidden="true">
      <circle cx="19" cy="19" r="16" fill="none" stroke="#d71f2b" stroke-width="3"/>
      <path d="M13 11c1-1 2.5-1 3 .3l1.3 3c.3.8 0 1.5-.6 2l-1.2 1c1 2.2 2.6 3.8 4.8 4.8l1-1.2c.5-.6 1.2-.9 2-.6l3 1.3c1.3.5 1.3 2 .3 3l-1.5 1.5c-1 1-2.7 1.2-4 .6-4.3-2-7.6-5.3-9.6-9.6-.6-1.3-.4-3 .6-4z" fill="#d71f2b"/>
    </svg>
    <span class="number">555-014-2290</span>
  </footer>
</main>
</body>
</html>
```